Food and Beverage Business Cards

We need business cards with logo designs for a consultant in the food and beverage industry. We specialize in helping restaurants fix operational and management problems.
Specific areas of expertise include:
-Steps of service
-Staff management tools
-Standard operating procedures
-Profit and loss management
-Inventory
-Point of sales
-Bar Menu
-Mystery shopper service
-Handling and managing suppliers

Target Market(s)

Restaurant and bar owners and managers

Industry/Entity Type

Business

Contact Information for Business Card

Mathieu Delorme
K&T Consulting
phone: 15027390618
mathkt@brindlemail.net

Font styles to use
Other font styles liked:
• Check out the screen shot font idea

Colors

Designer to choose colors to be used in the design.

Requirements
Must have
• Must include QR code (See attachment)
• Logo should reflect our specific focus on the drinks side of the industry.
• Areas of Expertise:
• -Service Steps
• -Staff management tools
• -S.O.P
• -P&L Management
• -Inventory
• -P.O.S
• -Bar Menu
• -Mystery Shopper Service
• -Handling and Managing Suppliers

```html
<!DOCTYPE html>
<html lang="en">
<head>
<meta charset="utf-8">
<title>Tidewell – Business Cards</title>
<link href="https://fonts.googleapis.com/css2?family=Open+Sans:wght@400;600;700&display=swap" rel="stylesheet">
<style>
  :root {
    --backdrop: #3a3a3c;
    --card-dark: #0d0d0d;
    --card-dark-edge: #1c1c1c;
    --card-light: #f7f7f7;
    --ink: #111111;
    --ink-soft: #2a2a2a;
    --on-dark: #f2f2f2;
    --on-dark-soft: #d6d6d6;
    --badge-green: #3a8f3c;
    --badge-grey: #6e6e6e;
    --badge-white: #e8e8e8;
  }
  * { box-sizing: border-box; margin: 0; padding: 0; }
  html, body { width: 1200px; height: 960px; overflow: hidden; }
  body {
    background: var(--backdrop);
    font-family: "Open Sans", Arial, sans-serif;
    position: relative;
  }
  .card {
    position: absolute;
    left: 220px;
    width: 760px;
    height: 410px;
    box-shadow: 0 14px 30px rgba(0,0,0,.45);
  }
  .card-back {
    top: 40px;
    background: linear-gradient(160deg, var(--card-dark-edge), var(--card-dark) 60%);
    color: var(--on-dark);
    text-align: center;
  }
  .badges {
    position: absolute;
    top: 26px;
    right: 30px;
    display: flex;
    gap: 12px;
  }
  .badge { width: 44px; height: 44px; border-radius: 50%; }
  .badge-green { background: var(--badge-green); }
  .badge-grey { background: var(--badge-grey); }
  .badge-white { background: var(--badge-white); }
  .brand {
    display: flex;
    align-items: center;
    justify-content: center;
    gap: 14px;
  }
  .brand-mark { width: 22px; height: 22px; background: currentColor; }
  .brand-name {
    font-weight: 600;
    font-size: 56px;
    line-height: 1;
  }
  .card-back .brand { margin-top: 118px; }
  .expertise-title {
    margin-top: 40px;
    font-weight: 700;
    font-size: 20px;
  }
  .expertise-list {
    margin-top: 8px;
    font-size: 15px;
    line-height: 1.6;
    color: var(--on-dark-soft);
    list-style: none;
  }
  .card-front {
    top: 500px;
    background: var(--card-light);
    color: var(--ink);
  }
  .edge-tab {
    position: absolute;
    top: 105px;
    width: 14px;
    height: 200px;
    background: var(--ink);
  }
  .edge-tab-left { left: 0; }
  .edge-tab-right { right: 0; }
  .contact {
    position: absolute;
    top: 72px;
    left: 44px;
  }
  .contact-name {
    font-weight: 700;
    font-size: 24px;
    text-transform: uppercase;
  }
  .contact-company {
    font-size: 17px;
    text-transform: uppercase;
    color: var(--ink-soft);
    margin-bottom: 12px;
  }
  .contact-line {
    display: flex;
    align-items: center;
    gap: 10px;
    font-size: 17px;
    color: var(--ink-soft);
    line-height: 1.5;
  }
  .contact-line svg { width: 15px; height: 15px; fill: var(--ink); }
  .card-front .brand {
    position: absolute;
    right: 70px;
    top: 200px;
  }
</style>
</head>
<body>
  <section class="card card-back" aria-label="Card back">
    <div class="badges">
      <span class="badge badge-green"></span>
      <span class="badge badge-grey"></span>
      <span class="badge badge-white"></span>
    </div>
    <div class="brand">
      <span class="brand-mark"></span>
      <span class="brand-name">Tidewell</span>
    </div>
    <h2 class="expertise-title">Areas of Expertise</h2>
    <ul class="expertise-list">
      <li>Service Steps | Staff management tools | S.O.P | P&amp;L Management</li>
      <li>Inventory | P.O.S | Bar Menu | Mystery Shopper Service</li>
      <li>Handling and Managing Suppliers</li>
    </ul>
  </section>

  <section class="card card-front" aria-label="Card front">
    <span class="edge-tab edge-tab-left"></span>
    <span class="edge-tab edge-tab-right"></span>
    <div class="contact">
      <h1 class="contact-name">Mathieu Delorme</h1>
      <p class="contact-company">K&amp;T Consulting</p>
      <p class="contact-line">
        <svg viewBox="0 0 16 16" aria-hidden="true"><path d="M3 2h3l1.5 3.5-2 1.2a8 8 0 0 0 3.8 3.8l1.2-2L14 10v3a1 1 0 0 1-1 1A11 11 0 0 1 2 3a1 1 0 0 1 1-1z"/></svg>
        15027390618
      </p>
      <p class="contact-line">
        <svg viewBox="0 0 16 16" aria-hidden="true"><path d="M1 3h14v10H1z M1 3l7 6 7-6" stroke="#f7f7f7" stroke-width="1"/></svg>
        mathkt@brindlemail.net
      </p>
    </div>
    <div class="brand">
      <span class="brand-mark"></span>
      <span class="brand-name">Tidewell</span>
    </div>
  </section>
</body>
</html>
```